Grand Opening / Live Music Event

My band is playing a Grand Opening event on Saturday April 5th. I need a flyer utilizing the attached image of our bass player and incorporating our band logo. This picture makes me laugh and gives the impression he is angry - like saying "it's going to be a celebration fool!" or something along those lines. I need to the flyer to pop and present an image that it will be an excellent party. Feel free to incorporate any background or theme style. You can find other images of my band in the event they are needed at: https://www.pagebook.example/Corvelbandfrisco

Some details:

The event will be at Brevan's Live. 8142 Oakridge Ave. #240, Frisco, Texas. (214) 555-0187 for table reservations.

Saturday April 5th. Party starts at 7:00 PM with an acoustic set by the Velvet Lanterns and Corvel taking the stage at 10:00 PM.

Hottest new bar in Frisco! Drink specials all night with the Harlow Pale girls, and great live music to celebrate this grand opening.

I will use this for FB and other online marketing, as well as some print.

```html
<!DOCTYPE html>
<html lang="en">
<head>
<meta charset="utf-8">
<title>Grand Opening – Brevan's Live</title>
<link rel="stylesheet" href="https://fonts.googleapis.com/css2?family=Audiowide&family=Archivo+Black&family=Tinos:wght@400;700&family=Oswald:wght@400&family=Arimo&family=Kaushan+Script&display=swap">
<style>
  :root {
    --bg: #000000;
    --headline-fill: #0a0a1e;
    --headline-edge: #3a5cff;
    --date-red: #ff1a2a;
    --date-edge: #2a3cff;
    --venue-blue: #2a36ff;
    --address-red: #ff1e1e;
    --lineup-green: #2cff2c;
    --entertain-green: #1c9a1c;
    --promo-red: #ff1010;
    --phone-blue: #2a36ff;
    --icon-blue: #3aa8e0;
    --logo-blue: #8fd3f0;
  }
  * { margin: 0; padding: 0; box-sizing: border-box; }
  html, body { width: 776px; height: 1200px; overflow: hidden; background: var(--bg); }
  .flyer { position: relative; width: 776px; height: 1200px; background: var(--bg); overflow: hidden; }

  .light-backdrop {
    position: absolute; left: 0; top: 60px; width: 776px; height: 800px;
    background:
      radial-gradient(ellipse 170px 170px at 300px 190px, rgba(235,235,245,.75), transparent 72%),
      radial-gradient(ellipse 200px 190px at 250px 360px, rgba(255,30,190,.9), transparent 72%),
      radial-gradient(ellipse 190px 230px at 640px 290px, rgba(255,235,20,.95), transparent 72%),
      radial-gradient(ellipse 130px 120px at 590px 130px, rgba(40,220,255,.6), transparent 72%),
      radial-gradient(ellipse 260px 90px at 360px 670px, rgba(255,120,60,.7), transparent 72%),
      radial-gradient(ellipse 200px 70px at 300px 700px, rgba(120,80,255,.6), transparent 72%),
      linear-gradient(180deg, #000 0%, #0a0610 45%, #000 100%);
  }

  .hero-photo {
    position: absolute; left: 262px; top: 220px; width: 300px; height: 500px;
    border-radius: 120px 120px 40px 40px;
    background:
      radial-gradient(ellipse 80px 60px at 150px 60px, rgba(255,200,230,.95), transparent 75%),
      linear-gradient(90deg, #ff2fa8 0%, #f26ac8 28%, #e8ecff 55%, #cfe9ff 72%, #f4e04a 100%);
    opacity: .92;
    box-shadow: 0 0 60px 20px rgba(255,255,255,.25);
  }

  .headline-svg { position: absolute; left: 0; top: 0; width: 776px; height: 200px; overflow: visible; }
  .headline-svg text {
    font-family: "Audiowide", sans-serif; fill: var(--headline-fill);
    stroke: var(--headline-edge); stroke-width: 2.5px; paint-order: stroke;
  }

  .event-date {
    position: absolute; right: 20px; top: 82px; text-align: center;
    font-family: "Archivo Black", sans-serif; font-size: 40px; line-height: 1.18;
    color: var(--date-red); -webkit-text-stroke: 1.5px var(--date-edge); letter-spacing: 2px;
  }

  .venue { position: absolute; left: 18px; top: 480px; font-family: "Tinos", serif; font-weight: 700; }
  .venue-title { color: var(--venue-blue); font-size: 38px; margin-left: 22px; text-shadow: 0 0 4px #fff; }
  .venue-address { color: var(--address-red); font-size: 26px; line-height: 1.4; margin-top: 4px; text-shadow: 0 0 3px #000; }

  .band-mark {
    position: absolute; left: 505px; top: 720px; display: flex; align-items: center; gap: 14px;
    transform: rotate(13deg);
    font-family: "Arimo", sans-serif; font-size: 54px; color: var(--logo-blue);
  }
  .band-mark-square { width: 36px; height: 36px; background: var(--logo-blue); }

  .section-title {
    position: absolute; left: 0; width: 776px; top: 796px; text-align: center;
    font-family: "Oswald", sans-serif; font-size: 50px; color: var(--entertain-green);
  }

  .lineup { position: absolute; left: 20px; top: 892px; list-style: none; font-family: "Arimo", sans-serif; font-size: 39px; color: var(--lineup-green); }
  .lineup li { display: flex; align-items: center; gap: 6px; height: 46px; white-space: nowrap; }
  .lineup-icon { width: 58px; height: 32px; flex: none; }

  .promo {
    position: absolute; left: 0; width: 776px; top: 1022px; text-align: center;
    font-family: "Kaushan Script", cursive; font-size: 34px; line-height: 1.1; color: var(--promo-red);
    white-space: nowrap;
  }

  .reservations {
    position: absolute; left: 0; width: 776px; top: 1126px; text-align: center;
    font-family: "Tinos", serif; font-size: 36px; letter-spacing: 1.5px; color: var(--phone-blue);
    white-space: nowrap;
  }
</style>
</head>
<body>
<main class="flyer">
  <div class="light-backdrop" role="img" aria-label="Neon pink, white and yellow light grids with sparkling streaks over colourful smoke"></div>
  <div class="hero-photo" role="img" aria-label="Photo of the band's bass player in a red tank top and white jeans holding a bass guitar, lit in pink and yellow"></div>

  <h1>
    <svg class="headline-svg" viewBox="0 0 776 200" aria-label="Grand Opening">
      <text x="36" y="84" font-size="92" textLength="706" lengthAdjust="spacingAndGlyphs" transform="skewX(-12) translate(14 0)">GRAND</text>
      <text x="28" y="180" font-size="72" textLength="386" lengthAdjust="spacingAndGlyphs" transform="skewX(-12) translate(34 0)">OPENING</text>
    </svg>
  </h1>

  <p class="event-date">SATURDAY<br>APRIL 5TH<br>@ 7:00 PM</p>

  <section class="venue">
    <h2 class="venue-title">Venue</h2>
    <p class="venue-address">Brevan's Live.<br>8142 Oakridge Ave. #240,<br>Frisco, Texas.</p>
  </section>

  <div class="band-mark"><span class="band-mark-square"></span>Corvel</div>

  <h2 class="section-title">Entertainment</h2>

  <ul class="lineup">
    <li>
      <svg class="lineup-icon" viewBox="0 0 58 32" aria-hidden="true"><circle cx="29" cy="16" r="14" fill="var(--icon-blue)"/></svg>
      Acoustic set by the Velvet Lanterns
    </li>
    <li>
      <svg class="lineup-icon" viewBox="0 0 58 32" aria-hidden="true"><rect x="14" y="2" width="30" height="28" fill="var(--icon-blue)"/></svg>
      Corvel take center stage @ 10:00 PM
    </li>
  </ul>

  <p class="promo">Hottest new bar in Frisco! Drink specials all night<br>with the Harlow Pale girls and great live music</p>

  <p class="reservations">Call:(214) 555-0187 For table Reservations</p>
</main>
</body>
</html>
```